Front Yard Sign for Real Estate Company

Bright Porch Keys is a brand new real estate broker. We need signs to put in front yard of houses that we are selling. 3D would be great. I have included the company LOGO

Target Market(s)

Residential Property buyers and sellers

Industry/Entity Type

Real Estate

Colors
ec1f27
ffc214
fbed22
ffffff

Requirements
Must have
• 3D look would be great. Logo must be included in the yard signs.
• Must include phone # to call: 614-290-4417

```html
<!DOCTYPE html>
<html lang="en">
<head>
<meta charset="utf-8">
<title>Bright Porch Keys – Yard Sign</title>
<link href="https://fonts.googleapis.com/css2?family=Montserrat:ital,wght@0,700;1,500&family=Oswald:wght@700&display=swap" rel="stylesheet">
<style>
  :root {
    --brand-red: #ec1f27;
    --brand-gold: #e8b623;
    --brand-yellow: #ffc214;
    --rule-gold: #c9a43a;
    --sign-white: #ffffff;
    --ink-dark: #3a2a2a;
    --backdrop: #eeeeee;
  }
  html, body {
    margin: 0;
    width: 965px;
    height: 1200px;
    overflow: hidden;
    background: var(--backdrop);
  }
  .canvas {
    width: 965px;
    height: 1200px;
    display: flex;
    align-items: center;
    justify-content: center;
  }
  .yard-sign {
    width: 865px;
    height: 579px;
    display: block;
    box-shadow: 0 4px 14px rgba(0,0,0,0.25);
    background: var(--sign-white);
  }
  .brand-name {
    font-family: "Montserrat", sans-serif;
    font-weight: 700;
    fill: var(--brand-red);
  }
  .tagline {
    font-family: "Montserrat", sans-serif;
    font-style: italic;
    font-weight: 500;
    fill: var(--brand-red);
  }
  .tagline-rule { stroke: var(--rule-gold); stroke-width: 1.4; }
  .brand-mark { fill: var(--brand-yellow); }
  .swoosh-gold { fill: var(--brand-gold); }
  .band-red { fill: var(--brand-red); }
  .phone-number {
    font-family: "Oswald", sans-serif;
    font-weight: 700;
    fill: var(--sign-white);
    stroke: var(--ink-dark);
    stroke-width: 2.2;
    paint-order: stroke fill;
    letter-spacing: 0.5px;
  }
</style>
</head>
<body>
<main class="canvas">
  <svg class="yard-sign" viewBox="0 0 575 385" xmlns="http://www.w3.org/2000/svg" role="img" aria-label="Bright Porch Keys yard sign with phone number 614-290-4417">
    <rect width="575" height="385" fill="var(--sign-white)"/>

    <g class="logo-lockup">
      <circle class="brand-mark" cx="287" cy="75" r="30"/>
      <text class="brand-name" x="287" y="173" text-anchor="middle" font-size="34">Bright Porch Keys</text>
      <line class="tagline-rule" x1="125" y1="192" x2="180" y2="192"/>
      <text class="tagline" x="287" y="196" text-anchor="middle" font-size="12.5">Selling Homes the Easy Way</text>
      <line class="tagline-rule" x1="394" y1="192" x2="450" y2="192"/>
    </g>

    <path class="swoosh-gold" d="M60 222 C220 215 400 200 530 186 L575 200 L575 214 C400 212 220 218 60 222 Z"/>
    <path class="band-red" d="M0 218 C200 222 400 212 575 210 L575 330 C400 330 200 340 0 356 Z"/>
    <path class="swoosh-gold" d="M0 358 C200 340 400 334 575 330 L575 338 C420 342 300 352 20 385 L0 385 Z"/>

    <text class="phone-number" x="287" y="312" text-anchor="middle" font-size="76">614-290-4417</text>
  </svg>
</main>
</body>
</html>
```